Automotive component supplier needs a business card design

We need a business card design for our company called Velmar Global Components Ltd based in the UK. We are a supplier of interior and exterior components to premium car manufacturers such as Corvane Hale, Durrant Fyfe, Maxtorn and Valdessimo. We would like to see a modern business card design that uses the colour blue.

Target Market(s)

Premium automotive car manufacturers.

Industry/Entity Type

Automotive

Contact Information for Business Card

Company Name : Velmar Global Components Limited
Address: 17 Tamsey Yard, Upper Drisk, Warwick, CV31 8RJ, United Kingdom
Web Address : www.velmarparts-example.co.uk

Font styles to use
Other font styles liked:
• Helvetica

Colors
3176b5
0255a3
85acd3
cfdeed
cee9f5
85cae6
34a6d7
0692cd
9bcb3c

Requirements
Must have
• Clear company logo and a mixture of blue colours.
Nice to have
• A high quality modern image.
Should not have
• Multiple colours.

```html
<!DOCTYPE html>
<html lang="en">
<head>
<meta charset="utf-8">
<title>Velmar Global Components – Business Card</title>
<link href="https://fonts.googleapis.com/css2?family=Montserrat:wght@400;500;600;700&display=swap" rel="stylesheet">
<style>
  :root {
    --blue-deep: #0255a3;
    --blue-main: #3176b5;
    --blue-bright: #0692cd;
    --blue-sky: #34a6d7;
    --lime: #9bcb3c;
    --white: #ffffff;
    --stage: #e9eef3;
  }
  * { box-sizing: border-box; margin: 0; padding: 0; }
  html, body { width: 1200px; height: 1000px; overflow: hidden; }
  body {
    background: var(--stage);
    font-family: "Montserrat", Helvetica, Arial, sans-serif;
    display: flex;
    flex-direction: column;
    align-items: center;
    justify-content: center;
    gap: 60px;
  }
  .card {
    width: 640px;
    height: 366px;
    border-radius: 22px;
    overflow: hidden;
    position: relative;
    box-shadow: 0 10px 28px rgba(2, 40, 80, 0.18);
  }

  /* Front */
  .card--front {
    background: radial-gradient(circle at 55% 35%, var(--blue-sky) 0%, var(--blue-main) 45%, var(--blue-deep) 100%);
    color: var(--white);
  }
  .brand {
    display: flex;
    align-items: center;
    gap: 12px;
    font-weight: 700;
    letter-spacing: 1px;
    text-transform: uppercase;
  }
  .brand__square { width: 18px; height: 18px; flex: none; }
  .card--front .brand {
    position: absolute;
    top: 120px;
    left: 0; right: 0;
    justify-content: center;
    font-size: 32px;
  }
  .card--front .brand__square { background: var(--white); }
  .legal-name {
    position: absolute;
    left: 0; right: 0;
    bottom: 52px;
    text-align: center;
    font-size: 17px;
    font-weight: 600;
    letter-spacing: 0.5px;
    text-transform: uppercase;
  }

  /* Back */
  .card--back { background: var(--white); }
  .card--back .brand {
    position: absolute;
    top: 66px;
    left: 0; right: 0;
    justify-content: center;
    font-size: 30px;
    color: var(--blue-bright);
  }
  .card--back .brand__square { background: var(--blue-bright); }
  .info-band {
    position: absolute;
    left: 0; right: 0; bottom: 0;
    height: 178px;
    background: linear-gradient(100deg, var(--blue-bright) 0%, var(--blue-main) 55%, var(--blue-deep) 100%);
    border-top: 5px solid var(--lime);
    display: flex;
    align-items: center;
    padding: 0 40px;
    color: var(--white);
  }
  .person {
    flex: 1;
    text-align: right;
    padding-right: 28px;
    font-size: 14px;
    line-height: 1.5;
  }
  .person__name {
    color: var(--lime);
    font-size: 22px;
    font-weight: 600;
    letter-spacing: 0.5px;
    line-height: 1.1;
  }
  .person__role { margin-bottom: 8px; }
  .divider {
    width: 1px;
    height: 120px;
    background: rgba(255,255,255,0.7);
  }
  .contacts {
    flex: 1;
    list-style: none;
    padding-left: 26px;
    font-size: 14px;
    line-height: 1.75;
  }
  .contacts li { display: flex; align-items: center; gap: 10px; }
  .contacts svg { width: 12px; height: 12px; flex: none; }
</style>
</head>
<body>

  <section class="card card--front" aria-label="Business card front">
    <div class="brand"><span class="brand__square"></span>Velmar Global Components</div>
    <p class="legal-name">Velmar Global Components Limited</p>
  </section>

  <section class="card card--back" aria-label="Business card back">
    <div class="brand"><span class="brand__square"></span>Velmar Global Components</div>

    <div class="info-band">
      <div class="person">
        <p class="person__name">HARLAN TESSOP</p>
        <p class="person__role">Director</p>
        <p>17 Tamsey Yard</p>
        <p>Upper Drisk, Warwick</p>
        <p>CV31 8RJ, United Kingdom</p>
      </div>
      <div class="divider"></div>
      <ul class="contacts">
        <li>
          <svg viewBox="0 0 12 12" aria-hidden="true"><path d="M2.5 1 L4.5 1 L5.2 3.5 L4 4.5 Q5 7 7.5 8 L8.5 6.8 L11 7.5 L11 9.5 Q10.5 11 9 11 Q1 10 1 2.5 Q1 1 2.5 1 Z" fill="#9bcb3c"/></svg>
          +330 2718-4052
        </li>
        <li>
          <svg viewBox="0 0 12 12" aria-hidden="true"><rect x="3" y="0.5" width="6" height="11" rx="1" fill="none" stroke="#9bcb3c" stroke-width="1.3"/><circle cx="6" cy="9.3" r="0.8" fill="#9bcb3c"/></svg>
          +330 2793-1164
        </li>
        <li>
          <svg viewBox="0 0 12 12" aria-hidden="true"><rect x="0.7" y="2.2" width="10.6" height="7.6" rx="1" fill="none" stroke="#9bcb3c" stroke-width="1.3"/><path d="M1 3 L6 6.8 L11 3" fill="none" stroke="#9bcb3c" stroke-width="1.2"/></svg>
          info@velmarparts-example.co.uk
        </li>
        <li>
          <svg viewBox="0 0 12 12" aria-hidden="true"><circle cx="6" cy="6" r="5.2" fill="none" stroke="#9bcb3c" stroke-width="1.2"/><ellipse cx="6" cy="6" rx="2.3" ry="5.2" fill="none" stroke="#9bcb3c" stroke-width="1"/><path d="M1 6 H11" stroke="#9bcb3c" stroke-width="1"/></svg>
          www.velmarparts-example.co.uk
        </li>
      </ul>
    </div>
  </section>

</body>
</html>
```